Tern Hollow Print and Mailing Services

We are looking for a website layout design for a direct print and mailing company which prints graphics, post cards, letters, does mailing and more.

Please see attached logo, as it will be used to match color scheme of website.

Current website:
www.ternhollowprintmail.com

Websites we like:
https://quillbaypressworks.com

Target Market(s)

Businesses / Media

Number of Pages Required

3 page

Font styles to use
Sans Serif

Requirements
Must have
• Color scheme to match logo

```html
<!DOCTYPE html>
<html lang="en">
<head>
<meta charset="utf-8">
<title>Tern Hollow Print and Mailing Services</title>
<link href="https://fonts.googleapis.com/css2?family=Open+Sans:wght@400;600;700;800&display=swap" rel="stylesheet">
<style>
:root{
  --red:#e3222a;
  --blue:#1150a4;
  --navy:#0c3f86;
  --green:#5bbb4a;
  --cyan:#3cbcef;
  --mint:#3ed598;
  --ink:#1d1d1d;
  --body:#555;
  --grey:#8a8a8a;
  --white:#fff;
}
*{box-sizing:border-box;margin:0;padding:0}
html,body{width:1200px;height:3579px;overflow:hidden}
body{font-family:"Open Sans",Arial,sans-serif;color:var(--body);background:var(--white);position:relative}
.abs{position:absolute}
/* header */
.site-header{position:absolute;top:0;left:0;width:1200px;height:138px;background:var(--white)}
.brand{left:95px;top:44px;display:flex;align-items:center;gap:12px}
.brand-dot{width:34px;height:34px;border-radius:50%;background:var(--blue)}
.brand-name{font-weight:800;font-size:24px;color:var(--blue);line-height:1}
.phone{left:745px;top:32px;display:flex;align-items:center;gap:10px;font-size:16px;color:var(--ink)}
.phone-icon{width:32px;height:32px;border-radius:50%;border:2px solid var(--green);display:flex;align-items:center;justify-content:center}
.quote-btn{left:966px;top:27px;width:134px;height:42px;background:var(--red);color:#fff;font-weight:700;font-size:14px;display:flex;align-items:center;justify-content:center}
.main-nav{right:100px;top:94px;display:flex;gap:24px;font-size:14px;font-weight:600;color:var(--ink)}
/* hero */
.hero{position:absolute;top:138px;left:0;width:1200px;height:525px;background:linear-gradient(100deg,#3a4452 0%,#5b6470 35%,#2b2f36 70%,#1b1d22 100%)}
.hero-title{left:573px;top:138px;font-size:50px;font-weight:800;color:#fff;letter-spacing:1px}
.hero-sub{left:573px;top:222px;width:540px;font-size:24px;font-weight:700;color:#fff;line-height:1.5}
.btn{display:flex;align-items:center;justify-content:center;color:#fff;font-weight:700;font-size:15px;height:44px}
.btn-upload{left:573px;top:334px;width:174px;background:var(--green)}
.btn-prepare{left:775px;top:334px;width:172px;background:var(--red)}
/* welcome */
.welcome{position:absolute;top:663px;left:0;width:1200px;height:482px}
.section-h{font-size:30px;font-weight:700;color:var(--ink);letter-spacing:.5px}
.welcome .section-h{left:98px;top:82px}
.welcome-text{left:98px;top:148px;width:525px;font-size:13px;line-height:1.75;color:var(--body)}
.welcome-text p{margin-bottom:14px}
.btn-more{left:98px;top:348px;width:152px;height:42px;background:var(--red);font-size:14px}
.video{left:637px;top:93px;width:394px;height:294px;border:4px solid #eee;background:linear-gradient(135deg,#9aa7b4,#5f6b79 60%,#3f4954)}
.play{left:833px-637px}
/* tiles */
.tiles{position:absolute;top:1145px;left:0;width:1200px;height:451px;display:grid;grid-template-columns:repeat(4,1fr);grid-template-rows:repeat(2,1fr);gap:13px 13px}
.tile{position:relative}
.tile.cyan{background:var(--cyan)}
.tile.mint{background:var(--mint)}
.tile .product{position:absolute;left:18%;top:18%;width:64%;height:64%;border-radius:4px}
.tile.feature{background:#1f9a55;display:flex;flex-direction:column;align-items:center;justify-content:center;gap:18px}
.feature-title{color:#fff;font-weight:800;font-size:20px}
.feature-btn{background:var(--red);color:#fff;font-weight:700;font-size:13px;padding:10px 18px}
/* services */
.services{position:absolute;top:1596px;left:0;width:1200px;height:537px;text-align:center}
.services .section-h{left:0;width:1200px;top:84px}
.services-intro{left:320px;top:140px;width:560px;font-size:13px;line-height:1.8}
.service{top:240px;width:230px}
.service svg{display:block;margin:0 auto}
.service h3{margin-top:24px;font-size:17px;font-weight:700;color:var(--ink)}
.service p{margin-top:12px;font-size:13px;line-height:1.75}
/* testimonials */
.testimonials{position:absolute;top:2133px;left:0;width:1200px;height:403px;background:linear-gradient(180deg,#2c2e33,#45474c 50%,#2a2b2e)}
.testimonials .section-h{left:0;width:1200px;top:78px;text-align:center;color:#fff}
.testi{top:168px;width:345px}
.avatar{position:absolute;left:0;top:10px;width:70px;height:70px;border-radius:50%;background:linear-gradient(135deg,#d7b9a2,#8c6d59);border:3px solid #fff}
.quote-mark{position:absolute;left:82px;top:-6px;font-size:34px;font-weight:800;color:#fff}
.testi-text{position:absolute;left:100px;top:4px;width:240px;font-size:12.5px;font-style:italic;line-height:1.75;color:#fff}
.testi-name{position:absolute;left:0;top:90px;font-size:13px;font-weight:700;color:#fff}
.testi-role{position:absolute;left:0;top:114px;font-size:12.5px;color:#eee}
.arrow{top:190px;color:#fff;font-size:22px}
/* news */
.news{position:absolute;top:2536px;left:0;width:1200px;height:685px}
.news .section-h{left:0;width:1200px;top:88px;text-align:center}
.news-intro{left:0;width:1200px;top:142px;text-align:center;font-size:13px}
.card{top:201px;width:312px}
.card-img{position:relative;height:186px;background:linear-gradient(135deg,#6f8aa6,#b9c4cf 60%,#5b6a7a)}
.date{position:absolute;left:15px;top:14px;width:52px;height:60px;background:var(--navy);color:#fff;text-align:center;font-size:13px;line-height:1.2;padding-top:8px}
.date b{display:block;font-size:20px}
.card h3{margin-top:22px;font-size:19px;font-weight:600;color:var(--ink);line-height:1.4}
.meta{margin-top:10px;font-size:12.5px;color:var(--body);display:flex;gap:18px;align-items:center}
.meta span{display:flex;align-items:center;gap:7px}
.card p{margin-top:14px;font-size:12.5px;line-height:1.75;height:44px}
.read{margin-top:22px;font-size:13px;font-weight:700;color:var(--red)}
/* footer */
.site-footer{position:absolute;top:3221px;left:0;width:1200px;height:358px;background:var(--navy);color:#fff}
.site-footer h4{font-size:15px;font-weight:700;color:#fff}
.links{left:100px;top:62px}
.links ul{list-style:none;margin-top:26px;font-size:12px;line-height:24px}
.links li::before{content:"›";margin-right:10px}
.contact{left:305px;top:62px}
.contact-row{display:flex;gap:18px;font-size:12px;line-height:1.7;margin-top:24px;align-items:flex-start}
.newsletter{left:589px;top:62px;width:260px}
.newsletter p{margin-top:24px;font-size:12px;line-height:1.7}
.email-field{margin-top:14px;width:254px;height:36px;border:1px solid #fff;font-size:12px;padding:9px 12px}
.subscribe{margin-top:14px;width:100px;height:30px;border-radius:15px;background:var(--red);font-size:12px;font-weight:700;display:flex;align-items:center;justify-content:center}
.badge{left:928px;top:62px;width:170px;height:105px;background:#e9edf4;border:3px solid #fff}
.socials{left:930px;top:198px;display:flex;gap:9px}
.socials span{width:36px;height:36px;border-radius:50%;border:2px solid #fff}
.foot-rule{left:100px;top:269px;width:1000px;height:1px;background:rgba(255,255,255,.35)}
.copyright{left:0;top:284px;width:1200px;text-align:center;font-size:13px}
</style>
</head>
<body>

<header class="site-header">
  <div class="abs brand"><span class="brand-dot"></span><span class="brand-name">Tern Hollow</span></div>
  <div class="abs phone">
    <span class="phone-icon"><svg width="16" height="16" viewBox="0 0 24 24"><path fill="#5bbb4a" d="M6.6 10.8a15 15 0 0 0 6.6 6.6l2.2-2.2c.3-.3.7-.4 1-.2 1.1.4 2.3.6 3.6.6.6 0 1 .4 1 1V20c0 .6-.4 1-1 1A17 17 0 0 1 3 4c0-.6.4-1 1-1h3.5c.6 0 1 .4 1 1 0 1.3.2 2.5.6 3.6.1.3 0 .7-.2 1z"/></svg></span>
    (+1) 555 014 7890
  </div>
  <div class="abs quote-btn">GET A QUOTE</div>
  <nav class="abs main-nav">
    <span>HOME</span><span>SERVICES &amp; PRINT PRODUCTS</span><span>QUOTES &amp; CUSTOM ORDERS</span><span>MY INVOICE ACCOUNT</span><span>MORE ▾</span>
  </nav>
</header>

<section class="hero" role="img" aria-label="Worker feeding a printed card into an industrial press">
  <h1 class="abs hero-title">TERN HOLLOW</h1>
  <p class="abs hero-sub">TernHollow Mailing Services, is proud to be both woman and minority owned.</p>
  <div class="abs btn btn-upload">UPLOAD FILES</div>
  <div class="abs btn btn-prepare">PREPARE FILES</div>
</section>

<section class="welcome">
  <h2 class="abs section-h">WELCOME TO TERN HOLLOW</h2>
  <div class="abs welcome-text">
    <p>Even in today's digital marketplace, mail continues to be one of the most effective forms of communication.</p>
    <p>TernHollow's mastery of the complexities of managed mail gives our clients the assurance that their mailings will be handled in the most professional, cost-effective, and efficient way possible. That means rapid results without the worry. You'll always get the optimum postage rates with our help.</p>
  </div>
  <div class="abs btn btn-more">READ MORE&nbsp;➜</div>
  <div class="abs video" role="img" aria-label="Video still of two staff reviewing work in a print shop">
    <svg class="abs" style="left:170px;top:120px" width="46" height="46" viewBox="0 0 46 46"><circle cx="23" cy="23" r="23" fill="#e3222a"/><path d="M18 13l14 10-14 10z" fill="#fff"/></svg>
  </div>
</section>

<section class="tiles">
  <div class="tile cyan"><div class="product" role="img" aria-label="Stack of brochures" style="background:linear-gradient(135deg,#f4efe3,#c9b58a)"></div></div>
  <div class="tile feature"><div class="feature-title">FREE PRINT SAMPLES</div><div class="feature-btn">GET A SAMPLE</div></div>
  <div class="tile cyan"><div class="product" role="img" aria-label="Business cards" style="background:linear-gradient(135deg,#222,#555 50%,#f5f5f5 51%)"></div></div>
  <div class="tile mint"><div class="product" role="img" aria-label="Roll of airmail labels" style="background:linear-gradient(135deg,#f3c21a,#16356e)"></div></div>
  <div class="tile cyan"><div class="product" role="img" aria-label="Letterhead and envelopes" style="background:linear-gradient(135deg,#fff,#e3222a)"></div></div>
  <div class="tile mint"><div class="product" role="img" aria-label="Colour swatch fan" style="background:linear-gradient(90deg,#e3222a,#f3c21a,#3ec24a,#1f6fd6,#8a2bb0)"></div></div>
  <div class="tile cyan"><div class="product" role="img" aria-label="Sale flyer" style="background:linear-gradient(135deg,#c8102e,#f6c343)"></div></div>
  <div class="tile mint"><div class="product" role="img" aria-label="Printed product box" style="background:linear-gradient(135deg,#f2f4f8,#27458f)"></div></div>
</section>

<section class="services">
  <h2 class="abs section-h">OUR SERVICES</h2>
  <p class="abs services-intro">We are housed in the former Alder Crest, California postal facility. Centrally located on a one-acre parcel with easy freeway access, our operations and administrative facilities comprise over 12,000 square feet.</p>
  <div class="abs service" style="left:97px">
    <svg width="70" height="66" viewBox="0 0 70 66"><rect x="18" y="4" width="34" height="18" fill="none" stroke="#1150a4" stroke-width="4"/><rect x="4" y="22" width="62" height="26" rx="3" fill="#e3222a"/><rect x="16" y="40" width="38" height="22" fill="#fff" stroke="#1150a4" stroke-width="4"/><circle cx="56" cy="30" r="3" fill="#fff"/></svg>
    <h3>LASER PRINTING</h3>
    <p>At vero eos et accusamus dignis ducim iditis praesentium voluptatum deleniti atque corrupti dolores</p>
  </div>
  <div class="abs service" style="left:353px">
    <svg width="70" height="66" viewBox="0 0 70 66"><path d="M16 4h28l12 12v46H16z" fill="none" stroke="#e3222a" stroke-width="5"/><path d="M35 48V24m-10 10l10-10 10 10" fill="none" stroke="#1150a4" stroke-width="5"/></svg>
    <h3>LETTERSHOP</h3>
    <p>At vero eos et accusamus dignis ducim iditis praesentium voluptatum deleniti atque corrupti dolores</p>
  </div>
  <div class="abs service" style="left:613px">
    <svg width="70" height="66" viewBox="0 0 70 66"><path d="M6 26L35 6l29 20v34H6z" fill="none" stroke="#e3222a" stroke-width="5"/><path d="M6 26l29 20 29-20" fill="none" stroke="#e3222a" stroke-width="5"/><path d="M22 22h26M22 30h26" stroke="#1150a4" stroke-width="4"/></svg>
    <h3>MAIL SORTING</h3>
    <p>At vero eos et accusamus dignis ducim iditis praesentium voluptatum deleniti atque corrupti dolores</p>
  </div>
  <div class="abs service" style="left:873px">
    <svg width="70" height="66" viewBox="0 0 70 66"><path d="M10 8l50 50" stroke="#1150a4" stroke-width="9"/><path d="M58 8L16 50l-6 10 10-6L62 12z" fill="#e3222a"/></svg>
    <h3>GRAPHIC DESIGN</h3>
    <p>At vero eos et accusamus dignis ducim iditis praesentium voluptatum deleniti atque corrupti dolores</p>
  </div>
</section>

<section class="testimonials" role="img" aria-label="Dim print shop floor with presses in the background">
  <h2 class="abs section-h">WHAT OUR CLIENTS SAY</h2>
  <div class="abs arrow" style="left:24px">‹</div>
  <div class="abs arrow" style="left:1166px">›</div>
  <div class="abs testi" style="left:97px">
    <div class="avatar" role="img" aria-label="Client portrait"></div><span class="quote-mark">“</span>
    <p class="testi-text">At vero eos et accusamus et iustodio dignissimos ducimus qui blanditiipraesent ium voluptatum deleniti atque corrupti quos dolores quas molestias</p>
    <div class="testi-name">MIRA DALE</div><div class="testi-role">Creative Manager, USA</div>
  </div>
  <div class="abs testi" style="left:444px">
    <div class="avatar" role="img" aria-label="Client portrait"></div><span class="quote-mark">“</span>
    <p class="testi-text">At vero eos et accusamus et iustodio dignissimos ducimus qui blanditiipraesent ium voluptatum deleniti atque corrupti quos dolores quas molestias</p>
    <div class="testi-name">TOM BRECKEN</div><div class="testi-role">Creative Manager, USA</div>
  </div>
  <div class="abs testi" style="left:787px">
    <div class="avatar" role="img" aria-label="Client portrait"></div><span class="quote-mark">“</span>
    <p class="testi-text">At vero eos et accusamus et iustodio dignissimos ducimus qui blanditiipraesent ium voluptatum deleniti atque corrupti quos dolores quas molestias</p>
    <div class="testi-name">IVO LASSEN</div><div class="testi-role">Creative Manager, USA</div>
  </div>
</section>

<section class="news">
  <h2 class="abs section-h">LATEST NEWS</h2>
  <p class="abs news-intro">Read The Latest News Regarding Our TernHollow Outstanding Service.</p>
  <article class="abs card" style="left:98px">
    <div class="card-img" role="img" aria-label="Operator at a printing press control panel"><div class="date">Feb<b>12</b></div></div>
    <h3>SwiftPress, Inc Receives 2010 Best of Alder Crest Award</h3>
    <div class="meta"><span>● Anvi</span><span>|</span><span>▭ 214 Comments</span></div>
    <p>For the second consecutive year, I am pleased to announce that 1:SwiftPress, Inc</p>
    <div class="read">Read More ➜</div>
  </article>
  <article class="abs card" style="left:444px">
    <div class="card-img" role="img" aria-label="Row of ink cartridges in a printer"><div class="date">Feb<b>12</b></div></div>
    <h3>Receives 2009 Best of Alder Crest Award (Tern Hollow Mailing)</h3>
    <div class="meta"><span>● Anvi</span><span>|</span><span>▭ 214 Comments</span></div>
    <p>I am pleased to announce that 1:SwiftPress, Inc (dba, TernHollow Mailing Services) has been</p>
    <div class="read">Read More ➜</div>
  </article>
  <article class="abs card" style="left:787px">
    <div class="card-img" role="img" aria-label="Large format paper rolls in a print room"><div class="date">Feb<b>12</b></div></div>
    <h3>Awarded Top 2008 Business - EquityTrade.net</h3>
    <div class="meta"><span>● Anvi</span><span>|</span><span>▭ 214 Comments</span></div>
    <p>EquityTrade.net is the nation's primary resource portal for business connections.</p>
    <div class="read">Read More ➜</div>
  </article>
</section>

<footer class="site-footer">
  <div class="abs links"><h4>QUICK LINKS</h4>
    <ul><li>Home</li><li>Our Services</li><li>Printing Products</li><li>Custom Orders</li><li>My Voice Account</li><li>Contact Us</li></ul>
  </div>
  <div class="abs contact"><h4>CONTACT US</h4>
    <div class="contact-row"><span>📍︎</span><span>48 Wren Lane, Parkway<br>CA 94500</span></div>
    <div class="contact-row"><span>☎︎</span><span>(+1) 555 014 7890</span></div>
    <div class="contact-row"><span>✉︎</span><span>info@ternhollowmailing.com</span></div>
  </div>
  <div class="abs newsletter"><h4>NEWSLETTER SUBSCRIPTION</h4>
    <p>Register your Email Address to get Information about us</p>
    <div class="email-field">Email Address</div>
    <div class="subscribe">SUBSCRIBE</div>
  </div>
  <div class="abs badge" role="img" aria-label="Business award badge"></div>
  <div class="abs socials"><span></span><span></span><span></span><span></span></div>
  <div class="abs foot-rule"></div>
  <div class="abs copyright">Copyrights © 2018 Tern Hollow. All Rights Reserved.</div>
</footer>

</body>
</html>
```